New International Co-Working Space Needs Pre-Registration Website

We need a simple but stylish pre-registration website for Nordcrest, a new international Coworking space. It needs to feature four sections: a description of the space, the benefits, the offering and a pre-registration form. We are looking for a clean, modern and simple yet stylish design. The site needs to be based on the divi wordpress theme. I have attached a more thorough briefing as well as our logo and some pictures we want to use.

Coding

Coded - Design and coding required

Number of Pages Required

3 page

```html
<!DOCTYPE html>
<html lang="en">
<head>
<meta charset="utf-8">
<title>Nordcrest — Co-Working Space</title>
<link rel="stylesheet" href="https://fonts.googleapis.com/css2?family=Roboto:wght@400;500;700;900&display=swap">
<style>
:root{
  --yellow:#efb61f;
  --ink:#1b1b1b;
  --white:#fff;
}
*{box-sizing:border-box;margin:0;padding:0}
html,body{width:1200px;height:3261px;overflow:hidden}
body{position:relative;background:var(--white);font-family:"Roboto",Arial,sans-serif;color:var(--ink)}
.abs{position:absolute}
.lorem{font-size:10px;line-height:15px;color:#333;text-align:justify}

/* top bar */
.topbar{left:0;top:0;width:1200px;height:26px;background:#fff;border-top:4px solid var(--yellow);border-bottom:1px solid #eee}
.topbar .dots{left:167px;top:5px;display:flex;gap:7px}
.topbar .dots span{width:11px;height:11px;border-radius:2px;background:#9a9a9a;display:block}
.topbar .links{right:167px;top:5px;font-size:9px;color:var(--yellow);letter-spacing:.5px;display:flex;gap:20px}

/* header */
.header{left:0;top:26px;width:1200px;height:61px;background:#fff}
.brand{display:flex;align-items:center;gap:9px;font-weight:700;font-size:30px;color:var(--ink);letter-spacing:-.5px}
.brand .mark{width:30px;height:30px;border-radius:50%;background:var(--yellow)}
.header .brand{left:167px;top:12px}
.nav{right:167px;top:24px;display:flex;gap:38px;font-size:11px;font-weight:500;color:#222}

/* hero */
.hero{left:0;top:87px;width:1200px;height:478px;background:linear-gradient(100deg,#0e0e0e 0%,#3a3631 35%,#6b5a45 50%,#2c2824 68%,#0d0d0d 100%)}
.form{left:739px;top:135px;width:294px;height:382px;background:rgba(10,10,10,.88)}
.form-head{left:0;top:0;width:294px;height:61px;background:var(--yellow);font-weight:900;font-size:28px;text-align:center;line-height:61px;color:var(--ink)}
.form-head::after{content:"";position:absolute;left:125px;top:61px;border:14px solid transparent;border-top:12px solid var(--yellow)}
.field{left:27px;width:240px;height:30px;border:1px solid #8a8a8a;color:#ddd;font-size:10px;padding:8px}
.submit{left:27px;top:312px;width:240px;height:38px;background:var(--yellow);font-weight:900;font-size:20px;text-align:center;line-height:38px;color:var(--ink)}

/* about */
.about-frame{left:167px;top:615px;width:244px;height:305px;border:13px solid var(--yellow)}
.about-photo{left:187px;top:635px;width:246px;height:309px;background:linear-gradient(135deg,#2a2a2a,#6b5040 55%,#b03a2e 80%,#3a2e28)}
.about-kicker{left:472px;top:636px;font-size:21px;color:#222}
.about-title{left:472px;top:659px;font-size:22px;font-weight:900;color:var(--yellow)}
.about-text{left:472px;top:692px;width:561px}
.about-text p+p{margin-top:6px}
.btn-outline{border:2px solid #222;font-size:10px;font-weight:700;text-align:center;color:#222}
.about .btn-outline{left:472px;top:843px;width:100px;height:31px;line-height:27px}
.info-chip{display:flex;align-items:center;gap:12px;font-size:11px;font-weight:700;line-height:15px}
.info-chip .ico{width:38px;height:38px;background:var(--yellow);display:flex;align-items:center;justify-content:center}
.about .brand.small{left:850px;top:902px;font-size:32px}
.brand.small .mark{width:34px;height:34px}

/* benefits */
.benefits-photo{left:0;top:993px;width:602px;height:457px;background:linear-gradient(120deg,#3a3633,#8a7868 40%,#c9b6a0 55%,#5e4c40 80%,#2a2522)}
.benefits{left:602px;top:993px;width:598px;height:457px;background:var(--yellow)}
.benefit{left:38px;display:flex;gap:12px;width:500px}
.benefit .num{flex:none;width:34px;height:34px;border-radius:50%;background:var(--ink);color:#fff;font-weight:700;font-size:17px;text-align:center;line-height:34px}
.benefit h3{font-size:18px;font-weight:500;line-height:20px;color:var(--ink)}
.benefit p{font-size:10px;line-height:14px;color:var(--ink)}

/* coworkers */
.section-title{left:0;width:1200px;text-align:center;font-size:29px;font-weight:900;color:var(--ink)}
.rule{left:570px;width:60px;height:4px;background:var(--yellow)}
.section-lead{left:200px;width:800px;text-align:center;font-size:10.5px;line-height:18px;color:#444}
.card{width:274px;height:196px}
.card .photo{position:absolute;left:0;top:0;width:274px;height:159px}
.card .cap{position:absolute;left:0;top:159px;width:274px;height:37px;background:var(--yellow);font-size:14px;font-weight:500;text-align:center;line-height:37px}

/* testimonial */
.testimonial{left:0;top:2102px;width:1200px;height:279px;background:linear-gradient(180deg,#1e1e1e,#262626)}
.avatar{left:552px;top:31px;width:96px;height:96px;border-radius:50%;border:4px solid var(--yellow);background:linear-gradient(160deg,#d8d4cf,#6d6f74)}
.quote{left:205px;top:148px;width:790px;text-align:center;font-size:10.5px;line-height:20px;color:#eee}
.quote-name{left:0;top:222px;width:1200px;text-align:center;font-size:13px;color:#eee}
.arrow{width:38px;height:38px;border-radius:50%;background:#8a8a8a;display:flex;align-items:center;justify-content:center;top:152px}

/* news */
.news-card{width:274px;height:167px;background:var(--yellow);text-align:center}
.news-card h4{margin-top:16px;font-size:14px;font-weight:700}
.news-card p{margin:20px auto 0;width:250px;font-size:13.5px;line-height:18px}
.news-card .btn-outline{position:absolute;left:92px;top:113px;width:90px;height:30px;line-height:26px;border-color:var(--ink)}

/* footer */
.footer{left:0;top:2757px;width:1200px;height:467px;background:linear-gradient(180deg,#252525,#1a1a1a)}
.kicker{font-size:12px;font-weight:700;color:var(--yellow)}
.foot-title{font-size:34px;font-weight:900;color:#fff;letter-spacing:-.5px}
.foot-lead{left:200px;top:104px;width:800px;text-align:center;font-size:10.5px;line-height:16px;color:#999}
.socials{left:494px;top:143px;display:flex;gap:13px}
.socials span{width:33px;height:33px;border-radius:50%;border:2px solid #bbb;display:block}
.col-kicker{font-size:9px;color:#aaa;letter-spacing:.5px}
.col-title{font-size:22px;font-weight:900;color:#fff;line-height:26px}
.col-text{font-size:9.5px;line-height:15px;color:#bbb}
.contact-line{display:flex;gap:10px;align-items:flex-start;font-size:10px;color:#ddd;padding:8px 0;border-top:1px solid #3a3a3a;width:232px}
.quick li{list-style:none;font-size:9.5px;color:#ccc;line-height:22px}
.quick li::before{content:"› ";color:#999}
.nl-field{width:272px;height:33px;border:1px solid #777;font-size:9.5px;color:#aaa;padding:10px}
.nl-btn{width:122px;height:37px;background:var(--yellow);color:var(--ink);font-size:11px;font-weight:700;text-align:center;line-height:37px}
.bottombar{left:0;top:3224px;width:1200px;height:37px;background:var(--yellow)}
.bottombar .copy{left:167px;top:13px;font-size:9px;color:var(--ink)}
.cards{right:167px;top:8px;display:flex;gap:5px}
.cards span{width:34px;height:21px;border-radius:3px;background:#fff;display:block}
.cards span:nth-child(2){background:#e9e9e9}
.cards span:nth-child(3){background:#2d4d9a}
.cards span:nth-child(4){background:#4f86d8}
</style>
</head>
<body>

<div class="topbar abs">
  <div class="dots abs"><span></span><span></span><span></span><span></span><span></span></div>
  <div class="links abs"><span>CONTACT</span><span>LANGUAGE</span></div>
</div>

<header class="header abs">
  <div class="brand abs"><span class="mark"></span>Nordcrest</div>
  <nav class="nav abs"><span>THE BEAUTIFUL SPACE</span><span>ALL THE GOODIES</span><span>THE OFFERING</span><span>PRE-REGISTER NOW</span></nav>
</header>

<section class="hero abs" role="img" aria-label="Barista pulling an espresso shot into a cup">
</section>
<form class="form abs">
  <div class="form-head abs">PRE-REGISTER</div>
  <div class="field abs" style="top:92px">Name...</div>
  <div class="field abs" style="top:136px">Email...</div>
  <div class="field abs" style="top:180px">Phone...</div>
  <div class="field abs" style="top:224px;height:72px">Message...</div>
  <div class="submit abs">SUBMIT</div>
</form>

<section class="about">
  <div class="about-frame abs"></div>
  <div class="about-photo abs" role="img" aria-label="Person writing in a red notebook beside a jar of iced tea"></div>
  <div class="about-kicker abs">NORDCREST</div>
  <div class="about-title abs">DISCOVER THE PLACE</div>
  <div class="about-text abs lorem">
    <p>Lorem Ipsum is simply dummy text of the printing and typesetting industry. Lorem Ipsum has been the industry's standard dummy text ever since the 1500s, when an unknown printer took a galley of type and scrambled it to make a type specimen book. It was popularised in the 1960s with the release of Letraset sheets containing Lorem Ipsum passages, and more recently with desktop publishing software like Aldus PageMaker including versions of Lorem Ipsum.</p>
    <p>Lorem Ipsum is simply dummy text of the printing and typesetting industry. Lorem Ipsum has been the industry's standard dummy text ever since the 1500s, when an unknown printer took a galley of type and scrambled it to make a type specimen book. It has survived not only five centuries, but also the leap into electronic typesetting, remaining essentially unchanged. It was popularised in the 1960s with the release of Letraset sheets containing Lorem Ipsum passages, and more recently with desktop publishing software like Aldus PageMaker including versions of Lorem Ipsum.</p>
  </div>
  <div class="btn-outline abs">READ MORE ›</div>
  <div class="info-chip abs" style="left:472px;top:905px">
    <span class="ico"><svg width="16" height="20" viewBox="0 0 16 20"><path d="M8 0a7 7 0 0 0-7 7c0 5 7 13 7 13s7-8 7-13a7 7 0 0 0-7-7zm0 10a3 3 0 1 1 0-6 3 3 0 0 1 0 6z" fill="#1b1b1b"/></svg></span>
    <span>480 LINDEN AVE. SUITE<br>210 HARBOR FALLS, OR</span>
  </div>
  <div class="info-chip abs" style="left:678px;top:905px">
    <span class="ico"><svg width="18" height="18" viewBox="0 0 24 24"><path d="M6.6 10.8a15 15 0 0 0 6.6 6.6l2.2-2.2c.3-.3.7-.4 1-.2 1.1.4 2.3.6 3.6.6.6 0 1 .4 1 1V20c0 .6-.4 1-1 1A17 17 0 0 1 3 4c0-.6.4-1 1-1h3.5c.6 0 1 .4 1 1 0 1.3.2 2.5.6 3.6.1.3 0 .7-.2 1z" fill="#1b1b1b"/></svg></span>
    <span style="font-size:17px">555.210.4870</span>
  </div>
  <div class="brand small abs"><span class="mark"></span>Nordcrest</div>
</section>

<section>
  <div class="benefits-photo abs" role="img" aria-label="Co-workers at a wooden table with drinks and glasses"></div>
  <div class="benefits abs">
    <div class="benefit abs" style="top:36px"><span class="num">1</span><div><h3>Exploration</h3><p>Lorem Ipsum is simply dummy text of the printing and typesetting industry.<br>Lorem Ipsum has been the industry's standard dummy text</p></div></div>
    <div class="benefit abs" style="top:103px"><span class="num">2</span><div><h3>Innovation</h3><p>Lorem Ipsum is simply dummy text of the printing and typesetting industry.<br>Lorem Ipsum has been the industry's standard dummy text</p></div></div>
    <div class="benefit abs" style="top:170px"><span class="num">3</span><div><h3>Technology</h3><p>Lorem Ipsum is simply dummy text of the printing and typesetting industry.<br>Lorem Ipsum has been the industry's standard dummy text</p></div></div>
    <div class="benefit abs" style="top:237px"><span class="num">4</span><div><h3>Creativity</h3><p>Lorem Ipsum is simply dummy text of the printing and typesetting industry.<br>Lorem Ipsum has been the industry's standard dummy text</p></div></div>
    <div class="benefit abs" style="top:304px"><span class="num">5</span><div><h3>Community</h3><p>Lorem Ipsum is simply dummy text of the printing and typesetting industry.<br>Lorem Ipsum has been the industry's standard dummy text</p></div></div>
    <div class="benefit abs" style="top:371px"><span class="num">5</span><div><h3>Community</h3><p>Lorem Ipsum is simply dummy text of the printing and typesetting industry.<br>Lorem Ipsum has been the industry's standard dummy text</p></div></div>
  </div>
</section>

<section>
  <h2 class="section-title abs" style="top:1494px">OUR CO-WORKERS</h2>
  <div class="rule abs" style="top:1536px"></div>
  <p class="section-lead abs" style="top:1568px">Lorem Ipsum is simply dummy text of the printing and typesetting industry. Lorem Ipsum has been the industry's standard dummy text ever since the 1500s, when an unknown printer took a galley of type and scrambled it to make a type specimen book.</p>
  <div class="card abs" style="left:167px;top:1635px"><div class="photo" role="img" aria-label="Woman presenting in a bright office" style="background:linear-gradient(135deg,#cfd6dc,#6f6a66 60%,#2e2a28)"></div><div class="cap">Lorem Ipsum dummy text</div></div>
  <div class="card abs" style="left:463px;top:1635px"><div class="photo" role="img" aria-label="Two colleagues smiling at a laptop" style="background:linear-gradient(135deg,#e2c9a4,#9a7048 55%,#3e3a38)"></div><div class="cap">Lorem Ipsum dummy text</div></div>
  <div class="card abs" style="left:759px;top:1635px"><div class="photo" role="img" aria-label="Team laughing around a computer" style="background:linear-gradient(135deg,#e0a070,#c05a3a 50%,#6a5a58)"></div><div class="cap">Lorem Ipsum dummy text</div></div>
  <div class="card abs" style="left:167px;top:1850px"><div class="photo" role="img" aria-label="Group meeting at a white table" style="background:linear-gradient(135deg,#e8e4de,#b88a6a 55%,#5a4e48)"></div><div class="cap">Lorem Ipsum dummy text</div></div>
  <div class="card abs" style="left:463px;top:1850px"><div class="photo" role="img" aria-label="Colleagues talking in a lounge" style="background:linear-gradient(135deg,#cfd2d6,#6f7278 55%,#2f3033)"></div><div class="cap">Lorem Ipsum dummy text</div></div>
  <div class="card abs" style="left:759px;top:1850px"><div class="photo" role="img" aria-label="Open-plan workspace with people at desks" style="background:linear-gradient(135deg,#f0efec,#b9b4ac 55%,#6b6560)"></div><div class="cap">Lorem Ipsum dummy text</div></div>
</section>

<section class="testimonial abs">
  <div class="avatar abs" role="img" aria-label="Portrait of the quoted member"></div>
  <p class="quote abs">Lorem Ipsum is simply dummy text of the printing and typesetting industry. Lorem Ipsum has been the industry's standard dummy text ever since the 1500s, when an unknown printer took a galley of type and scrambled it to make a type specimen book. It has survived not only five centuries, but also the leap into electronic recently with desktop publishing software like Aldus PageMaker including versions of Lorem Ipsum.</p>
  <div class="quote-name abs">Martin | Lakeview, CO</div>
  <div class="arrow abs" style="left:140px"><svg width="12" height="14" viewBox="0 0 12 14"><path d="M8 2 3 7l5 5" stroke="#fff" stroke-width="2" fill="none"/></svg></div>
  <div class="arrow abs" style="left:1031px"><svg width="12" height="14" viewBox="0 0 12 14"><path d="M4 2l5 5-5 5" stroke="#fff" stroke-width="2" fill="none"/></svg></div>
</section>

<section>
  <h2 class="section-title abs" style="top:2427px">NORDCREST NEWS</h2>
  <div class="news-card abs" style="left:167px;top:2518px"><h4>DECEMBER 2017</h4><p>Lorem Ipsum is simply dummy text<br>the printing and typesetting industry.</p><div class="btn-outline">READ MORE</div></div>
  <div class="news-card abs" style="left:463px;top:2518px"><h4>DECEMBER 2017</h4><p>Lorem Ipsum is simply dummy text<br>the printing and typesetting industry.</p><div class="btn-outline">READ MORE</div></div>
  <div class="news-card abs" style="left:759px;top:2518px"><h4>DECEMBER 2017</h4><p>Lorem Ipsum is simply dummy text<br>the printing and typesetting industry.</p><div class="btn-outline">READ MORE</div></div>
</section>

<footer class="footer abs">
  <div class="kicker abs" style="left:0;top:36px;width:1200px;text-align:center">SOCIAL PROFILES</div>
  <div class="foot-title abs" style="left:0;top:52px;width:1200px;text-align:center">FOLLOW US</div>
  <p class="foot-lead abs">Lorem Ipsum is simply dummy text of the printing and typesetting industry. Lorem Ipsum has been the industry's standard dummy text ever since the 1500s, when an unknown printer took a galley of type and scrambled it to make a type specimen book.</p>
  <div class="socials abs"><span></span><span></span><span></span><span></span><span></span></div>

  <div class="abs" style="left:167px;top:195px;width:240px">
    <div class="col-kicker">SHORTLY</div>
    <div class="col-title">ABOUT US</div>
    <p class="col-text" style="margin-top:12px;text-align:justify">Lorem Ipsum is simply dummy text of the printing and standard dummy text ever since the 1500s, when an unknown printer took a galley of type and scrambled it to make a type specimen good text book.</p>
    <div class="contact-line" style="margin-top:10px"><svg width="12" height="10" viewBox="0 0 12 10"><rect x=".5" y=".5" width="11" height="9" fill="none" stroke="#ddd"/><path d="M.5 .5 6 5l5.5-4.5" stroke="#ddd" fill="none"/></svg>info@nordcrest.com</div>
    <div class="contact-line" style="font-size:13px;font-weight:700"><svg width="12" height="12" viewBox="0 0 24 24"><path d="M6.6 10.8a15 15 0 0 0 6.6 6.6l2.2-2.2c.3-.3.7-.4 1-.2 1.1.4 2.3.6 3.6.6.6 0 1 .4 1 1V20c0 .6-.4 1-1 1A17 17 0 0 1 3 4c0-.6.4-1 1-1h3.5c.6 0 1 .4 1 1 0 1.3.2 2.5.6 3.6.1.3 0 .7-.2 1z" fill="#ddd"/></svg>(555) 318-2040</div>
    <div class="contact-line"><svg width="10" height="14" viewBox="0 0 16 20"><path d="M8 0a7 7 0 0 0-7 7c0 5 7 13 7 13s7-8 7-13a7 7 0 0 0-7-7zm0 10a3 3 0 1 1 0-6 3 3 0 0 1 0 6z" fill="#ddd"/></svg><span>Ridgeway Park 1140 - 72 Birchwood<br>Lane NE Halden, Ontario</span></div>
  </div>

  <div class="abs" style="left:452px;top:195px;width:240px">
    <div class="col-kicker">OUR</div>
    <div class="col-title">QUICK LINKS</div>
    <ul class="quick" style="margin-top:8px">
      <li>The beautiful space</li><li>All the goodies</li><li>The offering</li><li>Pre-register now</li><li>Contact Us</li><li>Careers</li><li>blog</li><li>FAQ</li>
    </ul>
  </div>

  <div class="abs" style="left:761px;top:195px;width:272px">
    <div class="col-kicker">JOIN</div>
    <div class="col-title">OUR NEWSLETTER</div>
    <div class="nl-field" style="margin-top:18px">Enter your email...</div>
    <div class="nl-field" style="margin-top:11px">Enter your password...</div>
    <div class="nl-btn" style="margin-top:16px">SUBSCRIBE NOW</div>
  </div>
</footer>

<div class="bottombar abs">
  <div class="copy abs">© 2017. NORDCREST.COM ALL RIGHT RESERVED</div>
  <div class="cards abs"><span></span><span></span><span></span><span></span></div>
</div>

</body>
</html>
```